Tarrowby Consulting needs a Business Catalogue

We are looking at creating a business catalogue that is used to introduce ourselves and our business as well as the services we offer. We are an HR business that offers assistance with recruitment and selection and all services involved in that area. We don't offer specific products and don't have prices advertised. it would be good to start with an introduction to the business and our history, some staff bios then a framework to discuss business scenarios where we can help. I would prefer white as the main colour on the front/back page with the colours of the logo (attached) to be used throughout the catalogue along with images and other visual improvements. A mall amount of colour should be used throughout and don't want solid colour pages. Prefer what pages that are broken up by coloured designs, images, diagrams heading etc. A 12-page catalogue with different designs I can move around as needed would be good.

Target Market(s)

Education, government, large business with administration staff

Font styles to use
Sans Serif

Requirements
Must have
• Logo colour scheme
• Images, diagrams, tables etc
• Start with company introduction (history, three staff profiles, company values etc)
• Main section will be the description of services and processes offered.
Nice to have
• A range of different visuals to choose from including designs for tables, paragraphs, diagrams, space for photos and other visual elements.

```html
<!DOCTYPE html>
<html lang="en">
<head>
<meta charset="utf-8">
<title>Tarrowby Consulting – Catalogue Pages</title>
<link href="https://fonts.googleapis.com/css2?family=Lato:wght@400;700;900&display=swap" rel="stylesheet">
<style>
:root{
  --stage:#3a3a3c;
  --paper:#ffffff;
  --blue:#1a90cf;
  --blue-light:#2aaee6;
  --blue-deep:#0f6fa8;
  --ink:#1d1d1f;
  --text:#3c3c3e;
  --grey-bar:#cfd0d2;
  --grey-box:#e6e7e9;
}
*{margin:0;padding:0;box-sizing:border-box}
html,body{width:876px;height:1200px;overflow:hidden;background:var(--stage)}
body{position:relative;font-family:'Lato',sans-serif;color:var(--text)}
.page{position:absolute;width:386px;background:var(--paper);overflow:hidden}
.page--front{left:41px;top:46px;height:547px}
.page--back{left:449px;top:46px;height:547px}
.page--why{left:41px;top:607px;height:546px}
.page--services{left:449px;top:607px;height:546px}
.abs{position:absolute}

.brand{position:absolute;top:100px;display:flex;align-items:center;gap:7px}
.brand__mark{width:18px;height:18px;background:var(--blue)}
.brand__name{font-weight:400;font-size:15px;letter-spacing:1px;color:var(--ink);line-height:1}
.brand__name small{display:block;font-size:6px;letter-spacing:3.2px;color:#8c8c8e;margin-top:2px}

.contact{left:32px;top:467px;font-size:10px;line-height:13px;color:var(--blue)}
.web-url{right:17px;top:492px;font-size:10px;color:var(--blue)}

.cover-title{left:32px;top:114px;color:#fff}
.cover-title__name{font-weight:900;font-size:30px;letter-spacing:0.5px;line-height:1}
.cover-title__sub{font-weight:700;font-size:10px;letter-spacing:6px;margin-top:4px}

.top-rule{left:34px;top:30px;width:329px;height:7px;background:var(--grey-bar)}
.top-tab{left:367px;top:30px;width:19px;height:7px;background:var(--blue)}

.why-heading{left:34px;top:80px;font-size:15px;font-weight:900;color:var(--ink);letter-spacing:0.2px}
.why-band{left:0;top:114px;width:386px;height:82px;background:var(--blue)}
.why-band-left{left:0;top:196px;width:226px;height:121px;background:var(--blue)}
.section{position:absolute;left:34px}
.section h3{font-size:8.5px;font-weight:700;margin-bottom:5px;text-transform:uppercase}
.section p{font-size:6.6px;line-height:9.2px;text-align:justify}
.section--on-blue{color:#fff}
.section--on-white h3{color:var(--ink)}

.services-stripe{left:0;top:0;width:138px;height:503px;background:var(--blue)}
.services-title{left:42px;top:78px;width:140px;height:25px;background:#d5d6d8;color:var(--blue-light);font-size:15px;font-weight:900;padding:2px 0 0 15px}
.service{position:absolute;left:42px;width:311px;height:51px}
.service__name{position:absolute;left:0;top:0;width:97px;height:51px;background:var(--blue-light);color:#fff;font-weight:700;font-size:12.5px;line-height:15px;padding:0 0 0 13px;display:flex;align-items:center}
.service__desc{position:absolute;left:108px;top:0;width:212px;height:51px;background:var(--grey-box);font-size:7px;line-height:9.3px;color:#4a4a4c;padding:8px 17px}
</style>
</head>
<body>

<!-- Front cover -->
<section class="page page--front">
  <div class="brand" style="left:39px">
    <span class="brand__mark"></span>
    <span class="brand__name">TARROWBY<small>CONSULTING</small></span>
  </div>
  <svg class="abs" style="left:0;top:0" width="386" height="547" viewBox="0 0 386 547">
    <defs>
      <linearGradient id="cityTone" x1="0" y1="0" x2="0" y2="1">
        <stop offset="0" stop-color="#bcdff2"/>
        <stop offset="0.45" stop-color="#3d8fc4"/>
        <stop offset="1" stop-color="#12507f"/>
      </linearGradient>
    </defs>
    <g role="img" aria-label="Photo of a city skyline with tall office towers in blue tones">
      <polygon points="206,91 386,91 386,466 171,466" fill="url(#cityTone)"/>
    </g>
    <polygon points="323,196 386,196 386,362 301,362" fill="var(--blue-light)" opacity="0.92"/>
  </svg>
  <div class="abs contact">Call: 123 555 0190<br>info@careerledger.com.au<br>www.careerledger.com.au</div>
</section>

<!-- Back cover -->
<section class="page page--back">
  <svg class="abs" style="left:0;top:0" width="386" height="547" viewBox="0 0 386 547">
    <defs>
      <linearGradient id="officeTone" x1="0" y1="0" x2="0" y2="1">
        <stop offset="0" stop-color="#d7e6f1"/>
        <stop offset="0.55" stop-color="#9fb6c6"/>
        <stop offset="1" stop-color="#e4edf3"/>
      </linearGradient>
    </defs>
    <polygon points="0,91 203,91 195,195 0,195" fill="var(--blue)"/>
    <polygon points="0,195 195,195 188,363 0,363" fill="var(--blue-light)"/>
    <polygon points="0,363 188,363 170,466 0,466" fill="var(--blue)"/>
    <g role="img" aria-label="Photo of an office desk with a laptop in front of windows overlooking a city">
      <rect x="111" y="195" width="258" height="193" fill="url(#officeTone)"/>
    </g>
  </svg>
  <div class="abs cover-title">
    <div class="cover-title__name">TARROWBY</div>
    <div class="cover-title__sub">CONSULTING</div>
  </div>
  <div class="brand" style="left:227px">
    <span class="brand__mark"></span>
    <span class="brand__name">TARROWBY<small>CONSULTING</small></span>
  </div>
  <div class="abs web-url">www.careerledger.com.au</div>
</section>

<!-- Why choose page -->
<section class="page page--why">
  <div class="abs top-rule"></div>
  <div class="abs top-tab"></div>
  <h2 class="abs why-heading">WHY CHOOSE CAREER LEDGER AUSTRALIA?</h2>
  <div class="abs why-band"></div>
  <div class="abs why-band-left"></div>
  <svg class="abs" style="left:226px;top:196px" width="160" height="251" viewBox="0 0 160 251">
    <defs>
      <linearGradient id="laptopTone" x1="0" y1="0" x2="1" y2="1">
        <stop offset="0" stop-color="#2f4f7a"/>
        <stop offset="0.5" stop-color="#8fa3c4"/>
        <stop offset="1" stop-color="#e3e8f2"/>
      </linearGradient>
    </defs>
    <g role="img" aria-label="Photo of hands typing on a laptop keyboard">
      <rect width="160" height="251" fill="url(#laptopTone)"/>
    </g>
  </svg>

  <div class="section section--on-blue" style="top:140px;width:330px">
    <h3>Quality Guarantee</h3>
    <p>I guarantee the quality of the work I deliver. My clients are afforded the opportunity to provide limitless feedback and request changes as often as required until they are 100% satisfied with the final product. It is extremely important to me that I create an application you are happy with and proud of and I will continue to work until that is achieved.</p>
  </div>
  <div class="section section--on-blue" style="top:199px;width:176px">
    <h3>Knowledge and Experience</h3>
    <p>The many years' experience I have in senior management positions within a number of public sector departments has given me an in-depth knowledge of the recruitment process, what makes a good application, what the panel is looking for and how to stand out from the crowd. This knowledge and experience is applied to your application to maximise your chance of securing an interview. Have a look at my profile to learn more about me.</p>
  </div>
  <div class="section section--on-white" style="top:339px;width:181px">
    <h3>Small Client Portfolio</h3>
    <p>Unlike the bigger, corporate service providers, I purposely maintain a small client portfolio to ensure I am able to provide each of my clients with the time and quality they deserve. I personally handle all correspondence and work that comes into my business to ensure continuity and quality. Your work won't be "delegated" to someone else to complete so you can be confident of the quality of work done.</p>
  </div>
  <div class="section section--on-white" style="top:447px;width:330px">
    <h3>Complete Start to Finish Service</h3>
    <p>I offer all types of application services from finding positions suitable for you to guiding you through submitting your application and all steps in between. Additionally, we can discuss your suitability for vacant positions, highlight your strengths and match those with the requirements of the position. Some of the more common services I offer include job search, cover letter, government criteria response, resume, online profile, application assistance and interview preparation.</p>
  </div>
</section>

<!-- Services page -->
<section class="page page--services">
  <div class="abs services-stripe"></div>
  <div class="abs top-rule" style="left:28px;width:335px"></div>
  <div class="abs top-tab"></div>
  <h2 class="abs services-title">MY SERVICES</h2>

  <div class="service" style="top:130px">
    <div class="service__name">Resume</div>
    <div class="service__desc">A resume is the first part of your application a panel member will see. It needs to be clear, concise and readable for maximum effect.</div>
  </div>
  <div class="service" style="top:187px">
    <div class="service__name">Government Criteria Response</div>
    <div class="service__desc">This is the most important part of your application and is the opportunity to highlight your skills, experience and suitability for the role.</div>
  </div>
  <div class="service" style="top:244px">
    <div class="service__name">Cover Letter</div>
    <div class="service__desc">Private sector letters generally do not require the same comprehensive criteria response that government letters do. But they are just as important for the same reasons.</div>
  </div>
  <div class="service" style="top:301px">
    <div class="service__name">Online Profile</div>
    <div class="service__desc">Nowadays, employers are looking increasingly for other avenues to assess applicants separate to their cover letter and resume. This can be a great advantage to an applicant if done properly.</div>
  </div>
  <div class="service" style="top:358px">
    <div class="service__name">Job Search</div>
    <div class="service__desc">It is important to find a job that matches what you want with your skills, education and experience. A proper job search will help locate suitable vacancies without compromising your dream job.</div>
  </div>
  <div class="service" style="top:415px">
    <div class="service__name">Interview Preparation</div>
    <div class="service__desc">You have been able to secure an interview. Now comes the most important part of turning the interview into an offer of employment. There are many techniques for interviewees to use.</div>
  </div>
</section>

</body>
</html>
```